The Pulp Corner- 2026 Menu- Drinks/Food

We are The Pulp Corner, a premium NYC-inspired juice bar.
We need two matching 4K TV menu designs with a clean, modern New York feel.
TV 1 – DRINKS
Cold-Pressed Juices, Smoothies, and Coffee/Espresso.
TV 2 – FOOD
Bowls, Toasts, Wraps, Hot Food, and Treats/Sweets.
The menus should feel bold, minimal, and easy to read from a distance.
Strong typography is preferred over heavy photos. The two screens must clearly match as one brand while serving different purposes.
Designs must be optimized for 4K TVs and in a NYC style (subtle subway / street influence, not cartoonish).
This is what we have now. We are updating items and prices along with changing some items.
I have some changes we’d like to do also. But this is what we are using now

```html
<!DOCTYPE html>
<html lang="en">
<head>
<meta charset="utf-8">
<title>The Pulp Corner – Food Menu</title>
<link href="https://fonts.googleapis.com/css2?family=Anton&family=Archivo+Black&family=Nunito:wght@400;700&display=swap" rel="stylesheet">
<style>
:root{
  --bg:#1f1f1f;
  --orange:#d85f27;
  --yellow:#f8e81c;
  --white:#ffffff;
  --ink:#111111;
  --muted:#e9e9e9;
}
*{margin:0;padding:0;box-sizing:border-box}
html,body{width:1200px;height:675px;overflow:hidden;background:var(--bg)}
.menu{position:relative;width:1200px;height:675px;background:linear-gradient(135deg,#242424,#1a1a1a);font-family:"Nunito",sans-serif;color:var(--white)}
.abs{position:absolute}
.section-bar{position:absolute;background:var(--orange);border-radius:4px;display:flex;align-items:center;justify-content:space-between;padding:0 14px 0 6px}
.section-bar h2{font-family:"Archivo Black",sans-serif;font-weight:400;color:var(--yellow);font-size:22px;letter-spacing:1px;line-height:1}
.mark{width:26px;height:26px;background:var(--ink);border-radius:2px}
.item{position:absolute;left:0;right:0}
.item-name{font-family:"Archivo Black",sans-serif;font-size:10px;letter-spacing:1px;line-height:12px;display:flex;justify-content:space-between}
.item-desc{font-size:9px;line-height:10.8px;margin-top:2px;color:var(--muted)}
.bowls{left:24px;top:67px;width:336px}
.bowls .item-desc{width:240px}
.parfaits{position:absolute;left:16px;top:443px;width:356px;height:215px;background:var(--orange);border-radius:4px}
.parfaits h2{position:absolute;left:10px;top:10px;font-family:"Archivo Black",sans-serif;font-weight:400;color:var(--yellow);font-size:20px;letter-spacing:1px}
.parfaits .mark{position:absolute;right:16px;top:8px}
.parfaits .list{position:absolute;left:8px;right:16px;top:0;bottom:0}
.parfaits .item-desc{color:var(--yellow);font-size:9.5px;width:290px}
.kicker{left:400px;width:442px;top:24px;text-align:center;font-family:"Archivo Black",sans-serif;font-size:15px;letter-spacing:7px}
.title-banner{left:400px;top:54px;width:442px;height:76px}
.title-banner svg{position:absolute;inset:0}
.title-banner h1{position:absolute;inset:0;display:flex;align-items:center;justify-content:center;font-family:"Anton",sans-serif;font-weight:400;color:var(--yellow);font-size:52px;letter-spacing:.5px;line-height:1}
.toasts{left:431px;top:206px;width:373px}
.toasts .item-desc{width:280px}
.custom{left:431px;top:575px;font-family:"Archivo Black",sans-serif;font-size:10px;letter-spacing:1px}
.custom small{display:block;font-family:"Nunito",sans-serif;font-size:7px;letter-spacing:0;margin-top:1px}
.legend{left:422px;top:611px;width:398px;height:48px;background:var(--orange);border-radius:4px}
.legend h3{position:absolute;left:0;right:0;top:6px;text-align:center;font-family:"Archivo Black",sans-serif;font-weight:400;font-size:16px;letter-spacing:1px}
.key{position:absolute;top:28px;display:flex;align-items:center;gap:7px;font-family:"Archivo Black",sans-serif;font-size:12px;letter-spacing:3px;color:var(--yellow)}
.key b{display:inline-flex;width:15px;height:15px;background:var(--ink);color:var(--yellow);justify-content:center;align-items:center;font-size:11px;letter-spacing:0;border-radius:2px}
.addons{font-family:"Archivo Black",sans-serif;font-size:6.8px;letter-spacing:.5px}
.addon{position:absolute;display:flex;justify-content:space-between;line-height:9px}
.addon small{display:block;font-family:"Nunito",sans-serif;font-size:5.6px;letter-spacing:.3px}
.col-a .addon{left:873px;width:148px}
.col-b .addon{left:1042px;width:137px}
.divider{left:1032px;top:68px;width:1px;height:152px;background:var(--orange)}
.social{left:893px;display:flex;align-items:center;gap:15px;font-family:"Archivo Black",sans-serif;font-size:17px;letter-spacing:1px}
.social i{display:block;width:46px;height:46px;background:var(--orange);border-radius:4px}
.notice{left:879px;top:363px;width:298px;height:59px;background:var(--orange);border-radius:3px;padding:3px;text-align:center;color:var(--ink)}
.notice p:first-child{font-size:11.5px;line-height:15px}
.notice p:last-child{margin-top:3px;background:var(--bg);color:var(--white);font-size:13px;line-height:14px;padding:2px 0 3px}
.notice p:last-child b{color:var(--yellow)}
.photos{left:870px;top:443px;width:312px;height:215px;background:var(--orange);border-radius:4px;padding:9px 8px 7px}
.photo{position:absolute;top:9px;height:199px}
.photo.subway{left:8px;width:186px;background:linear-gradient(160deg,#3a3328,#171614 55%,#5a4a24)}
.photo.bridge{left:198px;width:106px;background:linear-gradient(180deg,#d8c8a0,#8c6a40 55%,#3d2c1d)}
</style>
</head>
<body>
<main class="menu">

  <div class="section-bar" style="left:16px;top:22px;width:356px;height:34px"><h2>BOWLS</h2><span class="mark"></span></div>
  <div class="abs bowls">
    <div class="item" style="top:0"><div class="item-name"><span>PARK SLOPE</span><span>$13.50</span></div><p class="item-desc">Grade A Açai · Granola · Banana · Honey</p></div>
    <div class="item" style="top:30px"><div class="item-name"><span>BAY RIDGE</span><span>$12.50</span></div><p class="item-desc">Grade A Açai · Granola · Banana · Strawberries · Blueberries · Honey</p></div>
    <div class="item" style="top:71px"><div class="item-name"><span>BUSHWICK</span><span>$14.25</span></div><p class="item-desc">Grade A Açai · Granola · Banana · Pineapple · Fresh Coconut Meat · Honey · Bee Pollen</p></div>
    <div class="item" style="top:112px"><div class="item-name"><span>MAIN STREET</span><span>$14.00</span></div><p class="item-desc">Grade A Açai · Choice of Peanut, Almond, Cashew Butter or Hazelnut Spread · Granola · Banana · Honey · Cacao Nibs · Hemp Hearts</p></div>
    <div class="item" style="top:163px"><div class="item-name"><span>THE VILLAGE</span><span>$14.25</span></div><p class="item-desc">Grade A Açai · Choice of Peanut, Almond, Cashew Butter or Hazelnut Spread · Granola · Banana · Honey · Cacao Nibs · Hemp Hearts</p></div>
    <div class="item" style="top:214px"><div class="item-name"><span>BUILD YOUR OWN</span><span>$14.00</span></div><p class="item-desc">Grade A Açai · Granola · 2 Organic Fruits · Honey</p></div>
    <div class="item" style="top:244px"><div class="item-name"><span>PINK PITAYA</span><span>$14.00</span></div><p class="item-desc">Apple Juice blended w/ Pitaya · Banana · Strawberries Layered w/ Granola · Strawberries · Pineapple · Blueberries · Coconut Flakes · Honey · Hemp Hearts</p></div>
    <div class="item" style="top:295px"><div class="item-name"><span>CONEY ISLAND</span><span>$14.00</span></div><p class="item-desc">Coconut Milk blended w/ Coconut Chunks · Banana · Honey<br>Layered w/ Granola · Pineapple · Seasonal Fruit · Fresh Coconut Meat · Coconut Flakes · Honey · Hemp Hearts</p></div>
  </div>

  <section class="parfaits">
    <h2>PARFAITS &amp; TREATS</h2><span class="mark"></span>
    <div class="list">
      <div class="item" style="top:39px"><div class="item-name"><span>STARS &amp; STRIPES</span><span>$9.00</span></div><p class="item-desc">Vanilla Yogurt · Granola · Strawberries · Blueberries · Coconut Flakes · Honey · Hemp Hearts</p></div>
      <div class="item" style="top:82px"><div class="item-name"><span>BUILD YOUR OWN PARFAIT</span><span>$8.00</span></div><p class="item-desc">Vanilla Yogurt · Granola · Choice of 2 Fruits · Honey</p></div>
      <div class="item" style="top:113px"><div class="item-name"><span>PROTEIN BITES</span><span>$6.25</span></div><p class="item-desc">Coconut Milk · Greek Yogurt · Chia Seeds · Vanilla Extract · Maple Syrup · Choice of 2 Fruit Toppings · Coconut Flakes · Honey · Cinnamon</p></div>
      <div class="item" style="top:167px"><div class="item-name"><span>OVERNIGHT OATS</span><span>$9.00</span></div><p class="item-desc">Vanilla Yogurt · Granola · Strawberries · Blueberries · Coconut Flakes · Honey · Hemp Hearts</p></div>
    </div>
  </section>

  <p class="abs kicker">FOOD MENU</p>
  <div class="abs title-banner">
    <svg viewBox="0 0 442 76" width="442" height="76" aria-hidden="true">
      <path d="M30 4 H412 Q418 4 422 9 L440 38 L422 67 Q418 72 412 72 H30 Q24 72 20 67 L2 38 L20 9 Q24 4 30 4 Z" fill="#d85f27"/>
      <circle cx="38" cy="38" r="6" fill="#111"/><circle cx="404" cy="38" r="6" fill="#111"/>
    </svg>
    <h1>THE PULP CORNER</h1>
  </div>

  <div class="section-bar" style="left:422px;top:148px;width:398px;height:38px"><h2 style="font-size:23px">TOASTS &amp; WRAPS</h2><span class="mark" style="width:28px;height:28px"></span></div>
  <div class="abs toasts">
    <div class="item" style="top:0"><div class="item-name"><span>THE PATRIOT</span><span>$13.25</span></div><p class="item-desc">Seedy Sourdough · Choice of Peanut, Almond, Cashew Butter or Hazelnut Spread · Strawberries · Banana · Blueberries · Honey · Hemp Hearts</p></div>
    <div class="item" style="top:58px"><div class="item-name"><span>AVOCADO TOAST</span><span>$14.00</span></div><p class="item-desc">Seedy Sourdough · Whole Avocado · Everything Bagel Seasoning · Honey</p></div>
    <div class="item" style="top:104px"><div class="item-name"><span>BREAKFAST TOAST</span><span>$14.50</span></div><p class="item-desc">Seedy Sourdough · Smashed Avocado · Hard Boiled Eggs · Red Onion · Lemon Juice · Himalayan Pink Salt · Pepper · Everything Bagel Seasoning</p></div>
    <div class="item" style="top:162px"><div class="item-name"><span>SMOKED SALMON TOAST</span><span>$15.00</span></div><p class="item-desc">Seedy Sourdough · Smoked Wild Salmon · Tamari Sauce · Avocado · Cucumber · Leafy Greens · Everything Bagel Seasoning</p></div>
    <div class="item" style="top:219px"><div class="item-name"><span>TURMERIC CHICKEN SALAD</span><span>$15.00</span></div><p class="item-desc">Wholewheat Sprouted Grain Wrap · Mayo · Chicken Breast · Red Onion · Cucumber · Carrots · Leafy Greens · Balsamic Vinegar Dressing</p></div>
    <div class="item" style="top:279px"><div class="item-name"><span>ELITE WILD TUNA SALAD</span><span>$15.00</span></div><p class="item-desc">Wholewheat Sprouted Grain Wrap · Mayo · Wild Tuna · Red Onion · Celery · Leafy Greens</p></div>
    <div class="item" style="top:324px"><div class="item-name"><span>SPICY CHICKPEA SALAD (V)(S)</span><span>$14.00</span></div><p class="item-desc">Wholewheat Sprouted Grain Wrap · Tomatillo Sriracha · Chickpeas · Toasted Sesame Seeds · Red Pepper Hummus · Leafy Greens</p></div>
  </div>
  <p class="abs custom">CUSTOM<small>salads available upon request</small></p>

  <div class="abs legend">
    <h3>100% ORGANIC FRUITS &amp; VEGETABLES</h3>
    <span class="key" style="left:23px"><b>V</b>VEGAN</span>
    <span class="key" style="right:24px"><b>S</b>SPICY</span>
  </div>

  <div class="section-bar" style="left:870px;top:22px;width:312px;height:34px"><h2 style="font-size:21px">ADD-ONS &amp; MIX-INS</h2><span class="mark"></span></div>
  <div class="addons">
    <div class="col-a">
      <div class="addon" style="top:68px"><span>HONEY</span><span>$1.25</span></div>
      <div class="addon" style="top:80px"><span>EXTRA GRANOLA</span><span>$2.00</span></div>
      <div class="addon" style="top:92px"><span>GLUTEN FREE GRANOLA</span><span>$2.25</span></div>
      <div class="addon" style="top:104px"><span>COCONUT FLAKES</span><span>$2.00</span></div>
      <div class="addon" style="top:116px"><span>COCONUT OIL</span><span>$2.25</span></div>
      <div class="addon" style="top:128px"><span>BEE POLLEN</span><span>$2.00</span></div>
      <div class="addon" style="top:139px"><span>PEANUT BUTTER</span><span>$2.25</span></div>
      <div class="addon" style="top:151px"><span>ALMOND BUTTER</span><span>$2.50</span></div>
      <div class="addon" style="top:163px"><span>CASHEW BUTTER</span><span>$2.75</span></div>
      <div class="addon" style="top:175px"><span>HAZELNUT SPREAD</span><span>$2.75</span></div>
      <div class="addon" style="top:187px"><span>CHIA SEEDS</span><span>$2.00</span></div>
      <div class="addon" style="top:199px"><span>FLAX SEEDS</span><span>$2.00</span></div>
      <div class="addon" style="top:210px"><span>CACAO NIBS</span><span>$2.00</span></div>
    </div>
    <div class="abs divider"></div>
    <div class="col-b">
      <div class="addon" style="top:68px"><span>HEMP HEARTS</span><span>$2.00</span></div>
      <div class="addon" style="top:80px"><span>SPIRULINA</span><span>$2.00</span></div>
      <div class="addon" style="top:91px"><span>PLANT PROTEIN<small>(VANILLA OR CHOCOLATE)</small></span><span>$3.00</span></div>
      <div class="addon" style="top:109px"><span>WHEY PROTEIN<small>(VANILLA OR CHOCOLATE)</small></span><span>$3.25</span></div>
      <div class="addon" style="top:131px"><span>EXTRA ACAI</span><span>$3.25</span></div>
      <div class="addon" style="top:142px"><span>MACA POWDER</span><span>$2.50</span></div>
      <div class="addon" style="top:154px"><span>MORINGA POWDER</span><span>$2.75</span></div>
      <div class="addon" style="top:166px"><span>GOJI BERRIES</span><span>$2.25</span></div>
      <div class="addon" style="top:178px"><span>VANILLA YOGURT</span><span>$2.75</span></div>
      <div class="addon" style="top:190px"><span>GREEK YOGURT</span><span>$3.00</span></div>
      <div class="addon" style="top:201px"><span>AVOCADO</span><span>$3.25</span></div>
      <div class="addon" style="top:213px"><span>SEA MOSS GEL (V)</span><span>$4.00</span></div>
    </div>
  </div>

  <div class="abs social" style="top:242px"><i></i><span>THE PULP CORNER</span></div>
  <div class="abs social" style="top:299px"><i></i><span>@THEPULPCORNER212</span></div>

  <div class="abs notice">
    <p><b>12 Oz Juices</b> and <b>2 Oz Shots</b> served in glass bottles.</p>
    <p><b>Gallon</b> and <b>1/2 Gallon</b> of our signature juices<br>available upon request.</p>
  </div>

  <div class="abs photos">
    <div class="photo subway" role="img" aria-label="Photo of a subway train arriving at a station platform"></div>
    <div class="photo bridge" role="img" aria-label="Photo of a city bridge tower seen from a cobblestone street"></div>
  </div>

</main>
</body>
</html>
```